Online Media Company Website

Looking for a website design that clearly and powerfully portrays our brand. Vantorell. We are an online media technology company that helps advertisers understand the content and verify the context where they advertise in online video.

You can see more about our company at www.vantorell-example.tv and watch the video. The only thing you must keep is the logo (attached). Everything else is fair game.

We need the following sections:

Home
About Us
-Company
-Careers
-Management
Technology
-Publisher Solutions
-Advertiser Solutions
Press
Contact Us

On the main page should be a space where we can place our video plus showcase some important news such as whitepapers..etc.

Please include social media functions on the homepage such as twitter/facebook. Perhaps a section for a twitter feed.

Sites we like:
www.pelvagrin-example.com
www.quibbenlark-example.com
www.haskomelt-example.com
www.dorvanteq-example.com

Industry/Entity Type

Tv

Requirements
Nice to have
• social media feed

```html
<!DOCTYPE html>
<html lang="en">
<head>
<meta charset="utf-8">
<title>Vantorell — Online media technology company</title>
<link rel="stylesheet" href="https://fonts.googleapis.com/css2?family=Source+Sans+3:wght@400;600&family=Arimo:wght@400;700&display=swap">
<style>
:root{
  --blue-deep:#0b3f6e;
  --blue-mid:#1769a8;
  --blue-light:#6cc3ea;
  --page:#eeeeee;
  --ink:#333333;
  --body:#555555;
  --muted:#a5a5a5;
  --green:#7bbf1e;
  --footer:#232323;
  --footer-text:#c9c9c9;
  --teal:#1f6f8f;
  --head:"Source Sans 3", sans-serif;
  --text:"Arimo", sans-serif;
}
*{margin:0;padding:0;box-sizing:border-box}
html,body{width:1200px;height:900px;overflow:hidden}
body{position:relative;background:var(--page);font-family:var(--text);color:var(--body)}
.abs{position:absolute}
.hero-bg{position:absolute;left:0;top:0;width:1200px;height:380px}
.brand-tab{left:158px;top:-10px;width:274px;height:92px;background:#fff;border-radius:0 0 137px 137px/0 0 70px 70px;box-shadow:0 3px 6px rgba(0,0,0,.35);display:flex;align-items:center;justify-content:center;padding-top:8px}
.brand-name{font-family:var(--head);font-weight:400;font-size:38px;color:var(--teal);letter-spacing:.5px}
.main-nav{left:716px;top:31px;display:flex;align-items:center;gap:14px;font:700 10px var(--text);color:#fff}
.main-nav .current{background:linear-gradient(#5aa9e8,#2a78c4);border:1px solid #9fd0f5;border-radius:10px;padding:4px 15px}
.tagline{left:0;width:1180px;top:101px;text-align:center;font:400 18.5px var(--head);color:#fff}
.hero-title{left:156px;top:140px;font:400 43px/42px var(--head);color:#fff}
.hero-sub{left:157px;top:227px;font:400 18px var(--head);color:#fff}
.join-btn{left:428px;top:256px;width:130px;height:44px;border-radius:22px;background:linear-gradient(#5fb1ef,#1e63ad);box-shadow:0 3px 5px rgba(0,0,0,.35)}
.join-btn .arrow{left:14px;top:19px;width:0;height:0;border-left:4px solid #fff;border-top:3px solid transparent;border-bottom:3px solid transparent}
.join-btn .label{left:32px;top:8px;font:600 13px var(--head);color:#fff;line-height:13px}
.join-btn .small{left:32px;top:24px;font:400 9px var(--head);color:#bfe0f7}
.video-frame{left:657px;top:145px;width:338px;height:210px;background:#fff;padding:4px;box-shadow:0 4px 6px rgba(0,0,0,.5)}
.video-area{width:100%;height:100%;background:radial-gradient(circle at 50% 45%,#f1f1f1,#c8c8c8)}
h2.block-title{font:400 13px var(--head);color:var(--ink)}
.sub{font-size:8px;color:var(--muted)}
.copy{font-size:8.5px;line-height:13.5px;color:var(--body)}
.more{color:var(--green)}
.welcome{left:161px;top:387px;width:440px}
.column{top:529px;width:200px}
.thumb{width:199px;height:76px;margin:16px 0 10px}
.sidebar{left:789px;top:366px;width:212px}
.search{margin-top:10px;display:flex;width:198px;height:20px}
.search .field{flex:1;border:1px solid #d4d4d4;background:#fff;font-size:8px;color:#aaa;padding:5px 7px}
.search .go{width:19px;background:#333;border-radius:2px}
.service{position:absolute;left:0;width:214px}
.service .icon{position:absolute;left:0;top:4px;width:32px;height:32px}
.service .text{margin-left:52px}
.service h3{font:400 10px var(--text);color:var(--ink);margin-bottom:5px}
.service .copy{font-size:8px;line-height:14.5px;color:#888}
.divider{position:absolute;left:0;width:212px;height:1px;background:#dedede}
.footer{left:0;top:753px;width:1200px;height:147px;background:var(--footer)}
.footer h4{font:400 12px var(--text);color:#eee}
.footer .f-line{font-size:8px;color:var(--footer-text);line-height:15px}
.footer .accent{color:var(--green);font-weight:700}
.social{display:flex;gap:3px;margin-top:3px}
.social span{width:11px;height:11px;border-radius:2px}
</style>
</head>
<body>

<svg class="hero-bg" viewBox="0 0 1200 380" aria-hidden="true">
  <defs>
    <radialGradient id="heroGlow" cx="0.42" cy="0.85" r="0.7">
      <stop offset="0" stop-color="#7fd0f2"/>
      <stop offset="0.35" stop-color="#2b86c6"/>
      <stop offset="1" stop-color="#0a3865"/>
    </radialGradient>
  </defs>
  <rect width="1200" height="380" fill="url(#heroGlow)"/>
  <rect width="1200" height="4" fill="#1a1a1a"/>
  <path d="M0 376 C200 340 420 318 620 322 C820 326 1000 340 1200 368 L1200 380 L0 380 Z" fill="#eeeeee"/>
</svg>

<div class="abs brand-tab"><span class="brand-name">Vantorell</span></div>

<nav class="abs main-nav">
  <span class="current">Home</span><span>About Us</span><span>Technology</span><span>Press</span><span>Contact Us</span>
</nav>

<p class="abs tagline">We helps advertisers understand the content and verify the context where they advertise in online video</p>

<h1 class="abs hero-title">Online media<br>technology company</h1>
<p class="abs hero-sub">Each mount bilions of video streams</p>

<div class="abs join-btn">
  <span class="abs arrow"></span>
  <span class="abs label">JOIN TODAY</span>
  <span class="abs small">your future awaits</span>
</div>

<div class="abs video-frame">
  <div class="video-area" role="img" aria-label="Company video: billions of video streams each month"></div>
</div>

<section class="abs welcome">
  <h2 class="block-title">Welcome to Our Website</h2>
  <p class="sub">Lorem ipsum dolor sit amet, consectetur adipisicing elit, sed do eiusmod tempor</p>
  <p class="copy" style="margin-top:15px">Sed ut perspiciatis unde omnis iste natus error sit voluptatem accusantium mque laudantium, totam rem aperiam, eaque ipsa quae ab illo inventore veritatis et quasi architecto beatae vitae dicta sunt explicabo ullamco laboris nisi ut aliquip ex ea commodo consequat.</p>
  <p class="copy" style="margin-top:13px">Lorem ipsum dolor sit amet, consectetur adipisicing elit, sed do eiusmod tempor incididunt ut labore et dolore magna aliqua. <span class="more">read more... &gt;&gt;</span></p>
</section>

<section class="abs column" style="left:162px">
  <h2 class="block-title">Video Advertising</h2>
  <p class="sub">Sed congue, dui vel tristique mollis...</p>
  <div class="thumb" style="background:linear-gradient(120deg,#d7ecd9,#3f8a5c 45%,#1d4a33)" role="img" aria-label="Green abstract artwork"></div>
  <p class="copy">Lorem ipsum dolor sit amet, consectetur adipiscing elit. Mauris condimentum, libero ac hendrerit faucibus, urna urna fermentum nisl, vitae hendrerit nulla neque at orci.<br><span class="more">read more... &gt;&gt;</span></p>
</section>
<div class="abs" style="left:383px;top:530px;width:1px;height:192px;background:#dcdcdc"></div>
<section class="abs column" style="left:405px">
  <h2 class="block-title">Pending Technology</h2>
  <p class="sub">Sed congue, dui vel tristique mollis...</p>
  <div class="thumb" style="background:linear-gradient(90deg,#2a2a2a,#6b5a52 55%,#d9c7bd)" role="img" aria-label="Fashion photograph in dark tones"></div>
  <p class="copy">Sed imperdiet metus a augue dapibus vitae pulvinar dui semper. Nulla mi lacus, faucibus vitae venenatis eget, pharetra ac orci. Nullam blandit sapien leo.<br><br><span class="more">read more... &gt;&gt;</span></p>
</section>

<aside class="abs sidebar">
  <h2 class="block-title" style="font-weight:600;font-size:12px">Site Search:</h2>
  <div class="search"><span class="field">Search</span>
    <svg class="go" viewBox="0 0 19 20" aria-hidden="true"><rect width="19" height="20" rx="2" fill="#333"/><circle cx="8.5" cy="9" r="3.6" fill="none" stroke="#fff" stroke-width="1.5"/><line x1="11" y1="11.6" x2="14" y2="14.6" stroke="#fff" stroke-width="1.8"/></svg>
  </div>
  <h2 class="block-title" style="margin-top:34px">What Do We Do</h2>

  <div class="service" style="top:103px">
    <div class="icon" style="background:linear-gradient(#e0b57a,#b07a3a);border-radius:3px" role="img" aria-label="Package icon"></div>
    <div class="text"><h3>Video Playsment</h3><p class="copy">Curabitur sed urna id nunc pulvinar semper. Nunc sit amet tortor sit amet lacus sagittis<br><span class="more">read more... &gt;&gt;</span></p></div>
  </div>
  <div class="divider" style="top:174px"></div>
  <div class="service" style="top:189px">
    <div class="icon" style="background:linear-gradient(#555,#111);border-radius:4px" role="img" aria-label="Briefcase icon"></div>
    <div class="text"><h3>Works everywhere</h3><p class="copy">Curabitur sed urna id nunc pulvinar semper. Nunc sit amet tortor sit amet lacus sagittis<br><span class="more">read more... &gt;&gt;</span></p></div>
  </div>
  <div class="divider" style="top:261px"></div>
  <div class="service" style="top:278px">
    <svg class="icon" viewBox="0 0 32 32" aria-hidden="true"><rect x="0.5" y="0.5" width="31" height="31" fill="#fff" stroke="#999"/><path d="M0 8H32M0 16H32M0 24H32M8 0V32M16 0V32M24 0V32" stroke="#ddd"/><polyline points="3,26 10,18 16,22 22,12 29,8" fill="none" stroke="#333" stroke-width="1.5"/></svg>
    <div class="text" style="margin-left:49px"><h3>Power Your Projects</h3><p class="copy">Curabitur sed urna id nunc pulvinar semper. Nunc sit amet tortor sit amet lacus sagittis<br><span class="more">read more... &gt;&gt;</span></p></div>
  </div>
</aside>

<footer class="abs footer">
  <div class="abs" style="left:163px;top:16px;width:180px">
    <h4>What They Say</h4>
    <p class="f-line" style="margin-top:12px;color:#aaa"><span style="font:700 22px/8px var(--head);color:#ddd">&#8221;</span> "Quis autem vel eum iure reprehenderit qui in ea voluptate velit esse voluptas nulla pariatur?"</p>
    <p class="f-line accent">by: Dana Whitlock</p>
  </div>
  <div class="abs" style="left:436px;top:12px">
    <h4>News</h4>
    <p class="f-line" style="margin-top:10px">Lorem ipsum dolor sit amet<br><span class="accent">May 8th, 2015</span><br>Lorem ipsum dolor sit amet<br><span class="accent">May 15th, 2015</span><br>Lorem ipsum dolor sit amet<br><span class="accent">May 11th, 2015</span></p>
  </div>
  <div class="abs" style="left:643px;top:12px">
    <h4>Our Services</h4>
    <p class="f-line" style="margin-top:10px"><span class="accent">Video</span><br>Lorem ipsum dolor sit amet<br><span class="accent">Advertising</span><br>Lorem ipsum dolor sit amet<br><span class="accent">Playsment</span><br>Lorem ipsum dolor sit amet</p>
  </div>
  <div class="abs" style="left:869px;top:10px">
    <h4>Contact</h4>
    <p class="f-line" style="margin-top:10px"><b>+1 555.014.2290</b><br><span class="accent">hello@vantorell-example.tv</span><br>48 Larkfield Row<br>Brenmoor, ST 00417</p>
    <div class="social" aria-label="Social links"><span style="background:#4fb3e3"></span><span style="background:#3b5d9c"></span><span style="background:#f08a24"></span></div>
  </div>
</footer>

</body>
</html>
```